Income Tax Business Cards - Updates

Need to update these business cards while keeping all the same wording but just update them and make them look nicer and more modern/ on brand with our brand.

Industry/Entity Type

finance

Contact Information for Business Card

we have multiple locations so will just need to easily be able to change the address and phone numbers

Colors

Designer to choose colors to be used in the design.

```html
<!DOCTYPE html>
<html lang="en">
<head>
<meta charset="utf-8">
<title>Tax Call Card Design</title>
<link href="https://fonts.googleapis.com/css2?family=Montserrat:wght@400;500;600;700;800;900&display=swap" rel="stylesheet">
<style>
  :root {
    --brand-green: #275238;
    --brand-red: #c8343a;
    --ribbon-red: #e8424a;
    --ribbon-fold: #a8242b;
    --ink: #333333;
    --paper: #ffffff;
    --canvas: #f4f4f4;
    --edge: #d9d9d9;
  }
  * { box-sizing: border-box; margin: 0; padding: 0; }
  html, body {
    width: 1200px; height: 1200px; overflow: hidden;
    background: var(--canvas);
    font-family: "Montserrat", sans-serif;
  }
  .board { position: relative; width: 1200px; height: 1200px; }

  .panel-title {
    position: absolute; top: 340px; width: 502px;
    text-align: center; color: var(--brand-green);
    font-weight: 800; font-size: 27px; letter-spacing: 1.2px;
  }
  .panel-title--front { left: 72px; }
  .panel-title--back { left: 628px; }

  .card {
    position: absolute; top: 397px; width: 502px; height: 300px;
    background: var(--paper); border: 1px solid var(--edge);
    border-radius: 18px; overflow: hidden;
  }
  .card--front { left: 72px; }
  .card--back { left: 628px; }

  /* Front */
  .brand-row {
    position: absolute; left: 48px; right: 42px; top: 82px;
    display: flex; align-items: center; gap: 16px;
  }
  .brand {
    display: flex; align-items: center; gap: 8px; flex: none;
    color: var(--brand-green); font-weight: 700; font-size: 18px; white-space: nowrap;
  }
  .brand-mark { width: 12px; height: 12px; background: var(--brand-green); flex: none; }
  .rule { flex: 1; height: 3px; background: var(--brand-red); }

  .offer { position: absolute; left: 44px; top: 145px; color: var(--brand-red); }
  .offer-line { font-size: 15px; font-weight: 500; line-height: 20px; }
  .offer-line strong { font-weight: 700; }
  .offer-note { font-size: 9px; font-weight: 800; color: var(--brand-green); margin-top: 2px; }
  .ribbon { position: absolute; left: 34px; top: 206px; }
  .contact {
    position: absolute; right: 41px; top: 147px;
    text-align: right; color: var(--ink);
  }
  .contact-address { font-size: 13px; line-height: 20px; }
  .contact-phone { font-size: 20px; font-weight: 700; margin-top: 8px; }
  .contact-email { font-size: 13px; margin-top: 4px; }
  .foot-band {
    position: absolute; left: 0; bottom: 0; width: 100%; height: 18px;
    background: var(--brand-green);
  }

  /* Back */
  .headline { position: absolute; top: 46px; width: 100%; text-align: center; color: var(--brand-green); }
  .headline-small { font-size: 17px; font-weight: 800; letter-spacing: .5px; line-height: 20px; }
  .headline-big { font-size: 68px; font-weight: 900; line-height: 70px; letter-spacing: -1px; }
  .arc { position: absolute; left: 0; top: 0; }
  .arc-text { position: absolute; top: 200px; width: 100%; text-align: center; color: var(--paper); }
  .arc-line { font-size: 23px; font-weight: 500; line-height: 28px; }
  .arc-line strong { font-weight: 700; }
  .arc-web { font-size: 13px; margin-top: 10px; }
</style>
</head>
<body>
<main class="board">
  <h2 class="panel-title panel-title--front">FRONT CALL CARD DESIGN</h2>
  <h2 class="panel-title panel-title--back">BACK CALL CARD DESIGN</h2>

  <section class="card card--front">
    <div class="brand-row">
      <div class="brand"><span class="brand-mark"></span>Ledgerline Financial</div>
      <div class="rule"></div>
    </div>
    <div class="offer">
      <p class="offer-line">UP TO <strong>$6,000</strong></p>
      <p class="offer-line">SAME DAY ADVANCE</p>
      <p class="offer-note">ON APPROVED TAX RETURNS!</p>
    </div>
    <svg class="ribbon" width="200" height="56" viewBox="0 0 200 56">
      <polygon points="178,4 192,10 186,22 176,16" fill="var(--ribbon-fold)"/>
      <polygon points="8,14 180,8 190,40 12,50 2,32" fill="var(--ribbon-red)"/>
      <text x="98" y="34" text-anchor="middle" fill="#fff" font-family="Montserrat, sans-serif" font-weight="700" font-size="13" transform="rotate(-2 98 30)">FREE ESTIMATES!</text>
    </svg>
    <div class="contact">
      <p class="contact-address">4520 CEDAR ROW</p>
      <p class="contact-address">SUITE 310</p>
      <p class="contact-address">Springfield, OR 97477</p>
      <p class="contact-phone">(555)555-5555</p>
      <p class="contact-email">info@ledgerline.com</p>
    </div>
    <div class="foot-band"></div>
  </section>

  <section class="card card--back">
    <div class="headline">
      <p class="headline-small">FILE YOUR</p>
      <p class="headline-big">TAXES</p>
      <p class="headline-small">HERE</p>
    </div>
    <svg class="arc" width="502" height="300" viewBox="0 0 502 300">
      <path d="M0 250 Q251 110 502 250 V300 H0 Z" fill="var(--brand-red)"/>
    </svg>
    <div class="arc-text">
      <p class="arc-line">UP TO <strong>$6,000</strong></p>
      <p class="arc-line">SAME DAY ADVANCE</p>
      <p class="arc-web">www.ledgerline.com</p>
    </div>
  </section>
</main>
</body>
</html>
```